B2B Consulting firm needs a re-fresh of its process diagrams

We are a commercial real estate consulting firm. Think: I wonder who Korvanta uses when they have to build a new plant and sell the old one? That's us! We have created diagrams that we use to demonstrate to our clients the process of the project that they are about to go through. That is our "frontstage" diagram. We also have a "backstage" diagram that we use to train employees and to ensure that we do not make a stupid mistake! Here is a video showing you a little about what we are wanting https://view.clipmarrow.com/v/QpLRZW7BYEK4t8HJ2MVS

Target Market(s)

B2B - C-suite and business leaders

Industry/Entity Type

Commercial Real Estate

Font styles to use
Sans Serif

Colors
0094D4
00A9DD
6FCCEA
C7EBF8
E9F6FB
EB3D1F
EC4F4E
F09395
F8D3D4
FCEDEE

Requirements
Must have
• Think of it as a infographic - clean and modern
Nice to have
• I would suggest that you look at the infographics that are used by Pellingham Trade Journal, Drummoth, TVRL and other professional services firms/publications.

```html
<!DOCTYPE html>
<html lang="en">
<head>
<meta charset="utf-8">
<title>Larkfield Partners – Space Acquisition: Purchase &amp; Process Deliverables</title>
<link href="https://fonts.googleapis.com/css2?family=Montserrat:wght@400;500;600;700&family=Merriweather:wght@700;900&display=swap" rel="stylesheet">
<style>
  :root{
    --page:#a7a7ab;
    --slide:#eff0f7;
    --navy:#0e2237;
    --ink:#1c1c28;
    --rule:#9aa0ab;
    --white:#ffffff;
    --cyan:#1ba6df;
    --red:#e2432f;
    --teal-1:#41c2b9; --teal-2:#1c9b96; --teal-3:#0f6b6c; --teal-mark:#0f6b6c;
    --orange-1:#ee7561; --orange-2:#e0573f; --orange-3:#c8441f; --orange-mark:#ec5a2a;
    --purple-1:#6a3c9e; --purple-2:#4c2b7e; --purple-3:#341650; --purple-mark:#3b1c5c;
    --blue-1:#1f6f96; --blue-2:#17455e; --blue-3:#0f2638; --blue-mark:#122a3e;
    --dot-plan:#3ebfb5; --dot-eval:#ec5a45; --dot-exec:#5b3a9a; --dot-perf:#1f6f95;
  }
  *{margin:0;padding:0;box-sizing:border-box}
  html,body{width:1200px;height:1157px;overflow:hidden;background:var(--page)}
  body{position:relative;font-family:"Montserrat",sans-serif;color:var(--ink)}
  .slide{position:absolute;width:554px;height:312px;background:var(--slide);overflow:hidden;box-shadow:0 6px 10px rgba(0,0,0,.18)}

  /* cover */
  .cover-photo{position:absolute;inset:0;background:linear-gradient(120deg,#2a4b6e 0%,#1a3a5e 35%,#10284a 65%,#0a1c36 100%)}
  .cover-brand{position:absolute;left:0;width:100%;top:104px;text-align:center;color:var(--white)}
  .brand-name{font-family:"Montserrat",sans-serif;font-weight:500;color:var(--white);display:block;line-height:1}
  .cover-brand .brand-name.main{font-size:21px;letter-spacing:1px}
  .cover-brand .brand-name.sub{font-size:9px;letter-spacing:7px;margin-top:2px;padding-left:7px}
  .cover-kicker{position:absolute;left:145px;top:182px;font-family:"Merriweather",serif;font-weight:700;font-size:15px;color:var(--white);letter-spacing:.3px}
  .cover-title{position:absolute;left:143px;top:196px;font-family:"Merriweather",serif;font-weight:900;font-size:44px;line-height:1;color:var(--cyan);letter-spacing:1px}
  .cover-sub{position:absolute;left:147px;top:238px;font-family:"Merriweather",serif;font-weight:900;font-size:17.5px;color:var(--white);white-space:nowrap}
  .cover-sub .amp{color:var(--red);font-size:17px;margin-right:4px}

  /* brand tab */
  .brand-tab{position:absolute;right:0;top:0;width:126px;height:35px;background:var(--navy);border-bottom-left-radius:34px 35px;text-align:center;padding:10px 0 0 26px}
  .brand-tab .brand-name.main{font-size:11px;letter-spacing:.6px}
  .brand-tab .brand-name.sub{font-size:4.6px;letter-spacing:3.4px;margin-top:1px}

  /* stage track */
  .stage{position:absolute;top:46px;width:70px;text-align:center}
  .stage svg{width:15px;height:14px;display:block;margin:0 auto}
  .stage-label{font-family:"Merriweather",serif;font-weight:700;font-size:7.6px;color:#222;margin-top:2px;display:block}
  .track{position:absolute;left:24px;top:76px;width:505px;height:6px;border:1px solid var(--rule);border-radius:3px;background:var(--slide)}
  .track-fill{position:absolute;left:-1px;top:-1px;height:6px;border-radius:3px;background:var(--navy)}
  .dot{position:absolute;top:75px;width:8px;height:8px;border-radius:50%;background:var(--white);border:1px solid var(--rule)}
  .dot.plan{background:var(--dot-plan);border-color:var(--dot-plan)}
  .dot.eval{background:var(--dot-eval);border-color:var(--dot-eval)}
  .dot.exec{background:var(--dot-exec);border-color:var(--dot-exec)}
  .dot.perf{background:var(--dot-perf);border-color:var(--dot-perf)}

  /* column headers */
  .col-head{position:absolute;top:96px;height:27px;border-radius:3px;color:var(--white);font-family:"Merriweather",serif;font-weight:700;font-size:7.4px;display:flex;align-items:center;padding-left:12px;gap:12px}
  .col-head svg{width:17px;height:17px;flex:none}
  .col-head.process{left:81px;width:108px}
  .col-head.roles{left:207px;width:149px}
  .col-head.deliverables{left:374px;width:111px}
  .col-arrow{position:absolute;top:106px;width:0;height:0;border-top:3.5px solid transparent;border-bottom:3.5px solid transparent;border-left:6px solid #8c8c94}
  .col-arrow.a1{left:196px}.col-arrow.a2{left:363px}

  .teal .process{background:var(--teal-1)}.teal .roles{background:var(--teal-2)}.teal .deliverables{background:var(--teal-3)}
  .orange .process{background:var(--orange-1)}.orange .roles{background:var(--orange-2)}.orange .deliverables{background:var(--orange-3)}
  .purple .process{background:var(--purple-1)}.purple .roles{background:var(--purple-2)}.purple .deliverables{background:var(--purple-3)}
  .blue .process{background:var(--blue-1)}.blue .roles{background:var(--blue-2)}.blue .deliverables{background:var(--blue-3)}

  /* step marker */
  .step{position:absolute;left:24px;width:28px;height:36px}
  .step-circle{position:absolute;left:0;top:0;width:28px;height:28px;border-radius:50%;color:var(--white);font-family:"Merriweather",serif;font-weight:700;font-size:13px;display:flex;align-items:center;justify-content:center}
  .step-tip{position:absolute;left:9px;top:26px;width:0;height:0;border-left:5px solid transparent;border-right:5px solid transparent;border-top:8px solid var(--red)}
  .teal .step-circle{background:var(--teal-mark)}
  .orange .step-circle{background:var(--orange-mark)}
  .purple .step-circle{background:var(--purple-mark)}
  .blue .step-circle{background:var(--blue-mark)}

  /* content cards */
  .card{position:absolute;background:var(--white);border-radius:3px;box-shadow:0 1px 3px rgba(0,0,0,.16);font-size:5.2px;line-height:1.32;padding:7px 9px;color:var(--ink)}
  .card.c-process{left:81px;width:108px}
  .card.c-roles{left:207px;width:149px}
  .card.c-deliv{left:374px;width:111px}
  .card.dashed{box-shadow:none;border:.8px dashed #555;background:transparent}
  .card b{font-weight:700}
  .card ul{list-style:none}
  .card li{position:relative;padding-left:5px}
  .card li::before{content:"";position:absolute;left:0;top:2.1px;width:1.9px;height:1.9px;border-radius:50%;background:var(--ink)}
  .card .spaced li{margin-bottom:7px}
  .card .rule{border-top:.6px solid #333;margin:5px 0 4px}
  .card .cols{display:flex;gap:10px}
  .card .cols > div{flex:1}
  .card .gap{margin-top:5px}
  .divider{position:absolute;left:81px;width:404px;height:0;border-top:.8px solid var(--rule)}
</style>
</head>
<body>

<svg width="0" height="0" style="position:absolute" aria-hidden="true">
  <defs>
    <symbol id="ico-plan" viewBox="0 0 20 18"><g fill="none" stroke="#333" stroke-width="1"><rect x="1" y="2" width="11" height="14" rx="1"/><path d="M4 6h5M4 9h5M4 12h4"/><path d="M17 2l2 1.5-6 9-2.5 1 .5-2.5z"/></g></symbol>
    <symbol id="ico-eval" viewBox="0 0 22 18"><g fill="none" stroke="#333" stroke-width="1"><circle cx="11" cy="6" r="4.5"/><path d="M9 6l1.5 1.5L13.5 4.5"/><path d="M11 10.5v6"/><circle cx="3" cy="6" r="1.5"/><circle cx="19" cy="4" r="1.5"/><path d="M4.5 6h2M15.5 5l2-.6"/></g></symbol>
    <symbol id="ico-exec" viewBox="0 0 20 18"><g fill="none" stroke="#333" stroke-width="1"><path d="M18 1c-5 0-9 3-11 8l3 3c5-2 8-6 8-11z"/><circle cx="13" cy="6" r="1.5"/><path d="M7 9l-3 0-2 2 4 1M10 12l0 3-2 2-1-4"/><path d="M4 14l-2.5 2.5"/></g></symbol>
    <symbol id="ico-perf" viewBox="0 0 22 18"><g fill="none" stroke="#333" stroke-width="1"><path d="M3 14a8 8 0 0 1 16 0z"/><path d="M11 14l4-5"/><path d="M6 10l1 1M11 7v1.5M16 10l-1 1"/></g></symbol>
    <symbol id="ico-gear" viewBox="0 0 20 20"><g fill="none" stroke="#fff" stroke-width="1"><circle cx="10" cy="10" r="6.5"/><circle cx="10" cy="10" r="3"/><circle cx="10" cy="10" r="1"/><path d="M10 1v2.5M10 16.5V19M1 10h2.5M16.5 10H19M3.6 3.6l1.8 1.8M14.6 14.6l1.8 1.8M3.6 16.4l1.8-1.8M14.6 5.4l1.8-1.8"/></g></symbol>
    <symbol id="ico-roles" viewBox="0 0 20 20"><g fill="none" stroke="#fff" stroke-width="1"><circle cx="6" cy="4" r="2"/><path d="M3 9h6v5H8v5H4v-5H3z"/><circle cx="14" cy="6" r="2"/><path d="M11 11h6v4h-1v4h-4v-4h-1z"/></g></symbol>
    <symbol id="ico-deliv" viewBox="0 0 20 20"><g fill="none" stroke="#fff" stroke-width="1"><rect x="7.5" y="1.5" width="5" height="5"/><rect x="1.5" y="13.5" width="5" height="5"/><rect x="7.5" y="13.5" width="5" height="5"/><rect x="13.5" y="13.5" width="5" height="5"/><path d="M10 6.5v7M4 13.5v-3h12v3"/></g></symbol>
  </defs>
</svg>

<!-- Cover -->
<section class="slide cover" style="left:34px;top:51px">
  <div class="cover-photo" role="img" aria-label="Photograph of an industrial warehouse loading dock with roll-up doors at dusk, in deep blue tones"></div>
  <div class="cover-brand"><span class="brand-name main">LARKFIELD</span><span class="brand-name sub">PARTNERS</span></div>
  <div class="cover-kicker">SPACE ACQUISITION:</div>
  <div class="cover-title">PURCHASE</div>
  <div class="cover-sub"><span class="amp">&amp;</span>PROCESS DELIVERABLES</div>
</section>

<!-- Step 1 -->
<section class="slide teal" style="left:615px;top:51px">
  <div class="brand-tab"><span class="brand-name main">LARKFIELD</span><span class="brand-name sub">PARTNERS</span></div>
  <div class="stage" style="left:40px"><svg><use href="#ico-plan"/></svg><span class="stage-label">Planning</span></div>
  <div class="stage" style="left:171px"><svg><use href="#ico-eval"/></svg><span class="stage-label">Evaluation</span></div>
  <div class="stage" style="left:303px"><svg><use href="#ico-exec"/></svg><span class="stage-label">Execution</span></div>
  <div class="stage" style="left:435px"><svg><use href="#ico-perf"/></svg><span class="stage-label">Performance</span></div>
  <div class="track"><div class="track-fill" style="width:52px"></div></div>
  <span class="dot plan" style="left:71px"></span><span class="dot" style="left:202px"></span><span class="dot" style="left:334px"></span><span class="dot" style="left:466px"></span>
  <div class="col-head process"><svg><use href="#ico-gear"/></svg>Process</div><span class="col-arrow a1"></span>
  <div class="col-head roles"><svg><use href="#ico-roles"/></svg>Roles &amp; Responsibilities</div><span class="col-arrow a2"></span>
  <div class="col-head deliverables"><svg><use href="#ico-deliv"/></svg>Deliverables</div>

  <div class="step" style="top:125px"><div class="step-circle">1</div><span class="step-tip"></span></div>
  <div class="card c-process" style="top:129px;height:53px;padding-top:9px">
    <ul class="spaced"><li>Conduct Strategic Planning Define</li><li>Client Requirements</li><li>Create Budget &amp; Schedule</li></ul>
  </div>
  <div class="card c-roles" style="top:129px;height:167px">
    <div class="cols">
      <div><b>LPG Team</b><ul><li>Transaction Mgr</li><li>Portfolio Advisor</li><li>Broker</li><li>Project Mgr</li></ul>
        <div class="gap"><b>External Team</b><ul><li>Architect</li><li>Attorney</li><li>General Contractor</li><li>IT Consultant</li></ul></div></div>
      <div><b>Client Team</b><ul><li>Business Unit Mgr</li><li>Corporate RE Mgr</li><li>Risk Mgr</li><li>Regional Mgr</li><li>Local Operator</li><li>CEO/CFO</li><li>VP of Finance</li><li>Administrator</li></ul></div>
    </div>
    <div class="rule" style="margin-top:8px;margin-bottom:6px"></div>
    <ul><li>Evaluate requirement in light of client’s strategic plan; develop strategic plan, if appropriate.</li><li>Develop project management strategy, budget, and schedules.</li><li>Review critical action date report monthly.</li><li>Establish KPIs.</li><li>Distribute orientation binder.</li><li>Review existing LPG/Client customized</li><li>Playbooks for use and applicability.</li></ul>
  </div>
  <div class="card c-deliv" style="top:129px;height:119px">
    <b>Pre-Engagement Documents</b>
    <ul><li>Authorization Letter</li><li>Contact List</li><li>Contracts</li><li>RFQ Guidance</li><li>Service Level Agreement (2)</li><li>Commission Agreement</li><li>Standard Reporting Templates</li></ul>
    <div class="gap" style="margin-top:7px"><b>Client Needs Analysis (2)<br>Pre-Project Questionnaire</b></div>
    <div class="gap" style="margin-top:7px"><b>Strategic Plan (no deliverable)</b></div>
    <div class="gap" style="margin-top:7px"><b>Schedule and Budget</b></div>
  </div>
</section>

<!-- Steps 2–3 -->
<section class="slide orange" style="left:34px;top:395px">
  <div class="brand-tab"><span class="brand-name main">LARKFIELD</span><span class="brand-name sub">PARTNERS</span></div>
  <div class="stage" style="left:40px"><svg><use href="#ico-plan"/></svg><span class="stage-label">Planning</span></div>
  <div class="stage" style="left:171px"><svg><use href="#ico-eval"/></svg><span class="stage-label">Evaluation</span></div>
  <div class="stage" style="left:303px"><svg><use href="#ico-exec"/></svg><span class="stage-label">Execution</span></div>
  <div class="stage" style="left:435px"><svg><use href="#ico-perf"/></svg><span class="stage-label">Performance</span></div>
  <div class="track"><div class="track-fill" style="width:183px"></div></div>
  <span class="dot plan" style="left:71px"></span><span class="dot eval" style="left:202px"></span><span class="dot" style="left:334px"></span><span class="dot" style="left:466px"></span>
  <div class="col-head process"><svg><use href="#ico-gear"/></svg>Process</div><span class="col-arrow a1"></span>
  <div class="col-head roles"><svg><use href="#ico-roles"/></svg>Roles &amp; Responsibilities</div><span class="col-arrow a2"></span>
  <div class="col-head deliverables"><svg><use href="#ico-deliv"/></svg>Deliverables</div>

  <div class="step" style="top:140px"><div class="step-circle">2</div><span class="step-tip"></span></div>
  <div class="card c-process" style="top:143px;height:24px;padding-top:9px">Develop Negotiation Strategy</div>
  <div class="card c-roles" style="top:143px;height:24px"><b>Portfolio Advisor, Transaction Manager<br>and/or Broker</b></div>
  <div class="divider" style="top:185px"></div>

  <div class="step" style="top:201px"><div class="step-circle">3</div><span class="step-tip"></span></div>
  <div class="card c-process" style="top:201px;height:24px">Conduct Market Research and Analysis</div>
  <div class="card c-roles" style="top:201px;height:64px">
    <b>LPG Team, Client Team, External Team</b><div class="rule"></div>
    <ul><li>Develop market research comps to determine fair value,market availability, and cost.</li><li>Tour market with client and create shortlist of viable buildings.</li><li>Develop tour list and report to client.</li></ul>
  </div>
  <div class="card c-deliv" style="top:201px;height:51px;padding-left:13px">
    <ul><li>Market Survey Template</li><li>Financial Analysis</li><li>Own vs. Lease Analysis</li><li>Building Tour Spreadsheet</li><li>Building Tour Checklist</li></ul>
  </div>
</section>

<!-- Steps 4–6 -->
<section class="slide purple" style="left:615px;top:395px">
  <div class="brand-tab"><span class="brand-name main">LARKFIELD</span><span class="brand-name sub">PARTNERS</span></div>
  <div class="stage" style="left:40px"><svg><use href="#ico-plan"/></svg><span class="stage-label">Planning</span></div>
  <div class="stage" style="left:171px"><svg><use href="#ico-eval"/></svg><span class="stage-label">Evaluation</span></div>
  <div class="stage" style="left:303px"><svg><use href="#ico-exec"/></svg><span class="stage-label">Execution</span></div>
  <div class="stage" style="left:435px"><svg><use href="#ico-perf"/></svg><span class="stage-label">Performance</span></div>
  <div class="track"><div class="track-fill" style="width:315px"></div></div>
  <span class="dot plan" style="left:71px"></span><span class="dot eval" style="left:202px"></span><span class="dot exec" style="left:334px"></span><span class="dot" style="left:466px"></span>
  <div class="col-head process"><svg><use href="#ico-gear"/></svg>Process</div><span class="col-arrow a1"></span>
  <div class="col-head roles"><svg><use href="#ico-roles"/></svg>Roles &amp; Responsibilities</div><span class="col-arrow a2"></span>
  <div class="col-head deliverables"><svg><use href="#ico-deliv"/></svg>Deliverables</div>

  <div class="step" style="top:134px"><div class="step-circle">4</div><span class="step-tip"></span></div>
  <div class="card c-process" style="top:134px;height:24px;padding-top:9px">Negotiate with Short List</div>
  <div class="card c-roles" style="top:134px;height:38px">
    <b>Portfolio Advisor, Transaction Manager<br>and/or Broker</b>
    <div style="border-top:.6px solid #ccc;margin:3px 0 4px"></div><span style="padding-left:7px">Orchestrate competition.</span>
  </div>
  <div class="divider" style="top:182px"></div>

  <div class="step" style="top:190px"><div class="step-circle">5</div><span class="step-tip"></span></div>
  <div class="card c-process" style="top:192px;height:24px">Negotiate/Execute LOI and<br>Purchase &amp; Sale Agreement</div>
  <div class="card c-roles" style="top:192px;height:24px"><b>Portfolio Advisor, Transaction Manager<br>and/or Broker</b></div>
  <div class="card c-deliv" style="top:192px;height:24px;padding-left:13px"><ul><li>Letter of Intent</li><li>Purchase and Sale Agreement</li></ul></div>
  <div class="divider" style="top:227px"></div>

  <div class="step" style="top:241px"><div class="step-circle">6</div><span class="step-tip"></span></div>
  <div class="card c-process" style="top:237px;height:24px;padding-top:9px">Conduct Due Diligence</div>
  <div class="card c-roles" style="top:237px;height:63px">
    <b>Portfolio Advisor, Transaction Manager and/or Broker, Tax Specialist, Lender Rep, Client Legal, Client Risk, Third Party Vendors</b>
    <div class="rule"></div>
    <ul><li>Due diligence may include environmental, structural, A&amp;E, title, clarity, appraisal, financial appraisal, tax implications, etc.</li></ul>
  </div>
  <div class="card c-deliv" style="top:237px;height:24px;padding-left:13px"><ul><li>Closing Checklist</li><li>Due Diligence Checklist</li></ul></div>
</section>

<!-- Step 7 -->
<section class="slide purple" style="left:34px;top:739px">
  <div class="brand-tab"><span class="brand-name main">LARKFIELD</span><span class="brand-name sub">PARTNERS</span></div>
  <div class="stage" style="left:40px"><svg><use href="#ico-plan"/></svg><span class="stage-label">Planning</span></div>
  <div class="stage" style="left:171px"><svg><use href="#ico-eval"/></svg><span class="stage-label">Evaluation</span></div>
  <div class="stage" style="left:303px"><svg><use href="#ico-exec"/></svg><span class="stage-label">Execution</span></div>
  <div class="stage" style="left:435px"><svg><use href="#ico-perf"/></svg><span class="stage-label">Performance</span></div>
  <div class="track"><div class="track-fill" style="width:315px"></div></div>
  <span class="dot plan" style="left:71px"></span><span class="dot eval" style="left:202px"></span><span class="dot exec" style="left:334px"></span><span class="dot" style="left:466px"></span>
  <div class="col-head process"><svg><use href="#ico-gear"/></svg>Process</div><span class="col-arrow a1"></span>
  <div class="col-head roles"><svg><use href="#ico-roles"/></svg>Roles &amp; Responsibilities</div><span class="col-arrow a2"></span>
  <div class="col-head deliverables"><svg><use href="#ico-deliv"/></svg>Deliverables</div>

  <div class="step" style="top:138px"><div class="step-circle">7</div><span class="step-tip"></span></div>
  <div class="card c-process" style="top:136px;height:40px">Develop Move/Project Management Documentation &amp; Transition to Project Manager, if Applicable</div>
  <div class="card c-roles" style="top:136px;height:97px">
    <b>Portfolio Advisor, Transaction Manager and/or Broker, Project Manager, Relocation Manager, Lease Administrator</b>
    <div class="rule"></div>
    <ul><li>Transaction manager brings in other service line experts (project management, lease administration), if appropriate.</li><li>If LPG is performing project mgmt, see PM Playbook.</li><li>If LPG is not performing project mgmt, coordinate with client representative or landlord</li></ul>
  </div>
  <div class="card c-deliv dashed" style="top:208px;height:25px;padding-top:6px">See Project Management and Facilities Management Playbooks</div>
</section>

<!-- Step 8 -->
<section class="slide blue" style="left:615px;top:739px">
  <div class="brand-tab"><span class="brand-name main">LARKFIELD</span><span class="brand-name sub">PARTNERS</span></div>
  <div class="stage" style="left:40px"><svg><use href="#ico-plan"/></svg><span class="stage-label">Planning</span></div>
  <div class="stage" style="left:171px"><svg><use href="#ico-eval"/></svg><span class="stage-label">Evaluation</span></div>
  <div class="stage" style="left:303px"><svg><use href="#ico-exec"/></svg><span class="stage-label">Execution</span></div>
  <div class="stage" style="left:435px"><svg><use href="#ico-perf"/></svg><span class="stage-label">Performance</span></div>
  <div class="track"><div class="track-fill" style="width:505px"></div></div>
  <span class="dot plan" style="left:71px"></span><span class="dot eval" style="left:202px"></span><span class="dot exec" style="left:334px"></span><span class="dot perf" style="left:466px"></span>
  <div class="col-head process"><svg><use href="#ico-gear"/></svg>Process</div><span class="col-arrow a1"></span>
  <div class="col-head roles"><svg><use href="#ico-roles"/></svg>Roles &amp; Responsibilities</div><span class="col-arrow a2"></span>
  <div class="col-head deliverables"><svg><use href="#ico-deliv"/></svg>Deliverables</div>

  <div class="step" style="top:132px"><div class="step-circle">8</div><span class="step-tip"></span></div>
  <div class="card c-process" style="top:136px;height:24px">Measure/Demonstrate Performance</div>
  <div class="card c-roles" style="top:136px;height:74px">
    <b>Portfolio Advisor, Transaction Manager<br>and/or Broker</b>
    <div class="rule"></div>
    <ul><li>Benchmark performance and KPIs.</li><li>Submit client satisfaction forms.</li><li>Complete close-out summaries and corresponding critical date reports.</li><li>Create client case study, if transaction size meets criteria.</li></ul>
  </div>
  <div class="card c-deliv" style="top:136px;height:44px;padding-left:14px">
    KPI Documentation<br>Client Survey
    <ul style="margin-left:-5px"><li>Close-Out Package</li><li>Value-Added Matrix and Scorecard</li></ul>
  </div>
</section>

</body>
</html>
```